Discreet simple classy for adult entertainment

I would like a matte black business card with gold writing for my business. Keeping it simple. Having my following:

Lana frost
Events. Entertainment. Promotions
0491726580

or alternatively could have what i had on my previous card below but i think i prefer the above as again - discretion.

Maybe a nice gold line thru the card or some other very simple design . Or not open to ideas/ can be doublesided if any good ideas with that.

included pics of my old bus card. not sure weather i want a photo on it or not. if i do it wont be the same pic. i kinda wanted a card that was discreet so if it was in someones wallet they wouldn't neccessarily realise it was from a stripper.

Target Market(s)

men

Industry/Entity Type

Business

Contact Information for Business Card

Lana frost
0491726580

Requirements
Nice to have
• i don't know i am really open to anything. im giving my cards to guys so something they can have in their wallet that is discreet preferably.

```html
<!DOCTYPE html>
<html lang="en">
<head>
<meta charset="utf-8">
<title>Lana frost – business card</title>
<link href="https://fonts.googleapis.com/css2?family=Pinyon+Script&family=Jost:wght@300;400&display=swap" rel="stylesheet">
<style>
  :root {
    --backdrop: #3b3b3b;
    --backdrop-edge: #1e1e1e;
    --card-white: #ffffff;
    --card-black: #0b0b0b;
    --pattern-dark: #151515;
    --pattern-light: #232323;
    --gold-light: #f3dc8a;
    --gold-mid: #c9a13f;
    --gold-deep: #8a6a1e;
    --silver-text: #d4d4d4;
    --icon-ink: #111111;
    --photo-warm: #b89570;
    --photo-dark: #3a2c22;
  }
  * { box-sizing: border-box; margin: 0; padding: 0; }
  html, body { width: 1200px; height: 843px; overflow: hidden; }
  body {
    background: radial-gradient(ellipse at 50% 40%, var(--backdrop) 0%, var(--backdrop-edge) 100%);
    font-family: "Jost", sans-serif;
    position: relative;
  }
  .card {
    position: absolute;
    left: 290px;
    width: 620px;
    height: 344px;
    border-radius: 4px;
    box-shadow: 0 10px 30px rgba(0,0,0,0.55);
    overflow: hidden;
  }
  /* Front side */
  .card--front { top: 48px; background: var(--card-white); }
  .card__photo {
    position: absolute;
    top: 20px; left: 28px; right: 28px; bottom: 62px;
    border-radius: 26px;
    background: radial-gradient(ellipse at 45% 45%, var(--photo-warm) 0%, #6e5440 55%, var(--photo-dark) 100%);
  }
  .social-links {
    position: absolute;
    right: 30px; bottom: 20px;
    display: flex; gap: 18px;
    list-style: none;
  }
  .social-links__item {
    display: flex; align-items: center; gap: 6px;
    font-size: 13px; font-weight: 400; color: var(--icon-ink);
  }
  .social-links__dot {
    width: 14px; height: 14px; border-radius: 50%;
    background: var(--icon-ink);
  }
  /* Back side */
  .card--back {
    top: 448px;
    background: var(--card-black);
  }
  .card__pattern {
    position: absolute; inset: 0;
    background:
      radial-gradient(ellipse at 40% 30%, var(--pattern-light) 0%, transparent 55%),
      radial-gradient(ellipse at 75% 70%, var(--pattern-light) 0%, transparent 50%),
      linear-gradient(135deg, var(--pattern-dark), var(--card-black));
  }
  .brand-name {
    position: absolute;
    left: 58px; top: 58px;
    padding: 10px 40px 18px 12px;
    font-family: "Pinyon Script", cursive;
    font-weight: 400;
    font-size: 86px;
    line-height: 1;
    white-space: nowrap;
    background: linear-gradient(180deg, var(--gold-light) 0%, var(--gold-mid) 50%, var(--gold-deep) 100%);
    -webkit-background-clip: text;
    background-clip: text;
    color: transparent;
  }
  .contact-row {
    position: absolute;
    left: 240px; top: 205px;
    display: flex; align-items: center;
  }
  .phone {
    font-weight: 300;
    font-size: 30px;
    letter-spacing: 1px;
    color: var(--silver-text);
    margin-right: 22px;
  }
  .divider {
    width: 1px; height: 90px;
    background: var(--silver-text);
    opacity: 0.8;
    margin-right: 18px;
  }
  .services {
    list-style: none;
    font-weight: 300;
    font-size: 18px;
    letter-spacing: 0.5px;
    line-height: 1.2;
    text-transform: uppercase;
    color: var(--silver-text);
    padding-top: 18px;
  }
</style>
</head>
<body>
  <section class="card card--front">
    <div class="card__photo" role="img" aria-label="Portrait photograph of the performer"></div>
    <ul class="social-links">
      <li class="social-links__item"><span class="social-links__dot"></span>Flick</li>
      <li class="social-links__item"><span class="social-links__dot"></span>Pinbox</li>
      <li class="social-links__item"><span class="social-links__dot"></span>Chatter</li>
    </ul>
  </section>

  <section class="card card--back">
    <div class="card__pattern" role="img" aria-label="Subtle black damask pattern"></div>
    <h1 class="brand-name">Lana frost</h1>
    <div class="contact-row">
      <span class="phone">0491726580</span>
      <span class="divider"></span>
      <ul class="services">
        <li>Events</li>
        <li>Entertainment</li>
        <li>Promotions</li>
      </ul>
    </div>
  </section>
</body>
</html>
```